Corporate ID design for Financial Services/Accountant Company - brochure, flyer, letterhead, email s

Hi designers :)

Torvela Financial Services requires a corporate ID design look and feel for all their ongoing items moving forward. It needs to be highly professional looking, corporate, contemporary and a standout design!

Items needed:
Letterhead design + follow-on header for 2nd and 3rd pages etc.
Tri-fold (or similar) brochure design
Flyer (A5) for mailout
Client form design
Email Signature Design

A boutique financial management company providing services in: Accounting, Bookkeeping, Payroll, Consulting services to corporate small & large clientele in Australia. The design needs to run across all items, matching them together to communicate professionalism, finance and style.

Logo needs to be on all items, however the design across all items can be completely different as long as it works in the logo (i.e don't want footprints over whole designs as it doesn't communicate hi-end corporate feel).

Would like a beautifully designed graphic element/design style included across all items to match together and become part of the corporate identity/branding.

Fresh, clean, modern, corporate and professional style.

ITEMS - how they will be used>
Letterhead - Will be used mainly online so design needs to be able to go into WORD document to edit over.

A5 flyer - will be printed on high gloss card. Needs to be double sided full colour for print with 3mm bleed

Tri-fold brochure - will be printed as well, needs to be standard print size, full cmyk colour both sides and it will be handed out to new clients for more information on prices & staff etc

Email signature - Just a nice simple and clean design with matching element from above items.

Client Form - needs to be laid out with a nice design in indesign please.

Thanks & look forward to your submissions!

Target Market(s)

Target market is professional businesses wanting financial and bookkeeping services delivered with exceptional service.

Industry/Entity Type

Financial

Requirements
Must have
• Logo
• Work in corporate/logo colours.
• Would like final files created in indesign if possible please. Graphics and illustration are fine in illustrator first.
• Design with some or a element from website to match everything together>
• http://www.torvela.com.au/
Nice to have
• Would love to see some designs in the blue, with creative designs/illustrations in background watermark (i.e opacity of grey showing a hint of a design across all items)
• Could work in the orange from website text if it looks good on some areas.
Should not have
• Don't want footprints over all items as the whole design. We want a new creative look and feel (corporate & professional) but just working in the logo. Can include PARTS of the footprint &/or logo in design across items.

```html
<!DOCTYPE html>
<html lang="en">
<head>
<meta charset="utf-8">
<title>Torvela Financial Services – A5 Flyer</title>
<link href="https://fonts.googleapis.com/css2?family=Arimo:wght@400;700&family=Libre+Baskerville:wght@400;700&family=Great+Vibes&display=swap" rel="stylesheet">
<style>
:root{
  --board:#cbcbcb;
  --ink:#111;
  --brand-blue:#04679a;
  --heading-blue:#0a6aa1;
  --band-grey:#58595b;
  --body-grey:#444;
  --icon-grey:#5a5a5a;
  --paper:#fff;
  --photo-light:#dfe7f1;
  --photo-mid:#b9cce4;
}
*{margin:0;padding:0;box-sizing:border-box}
html,body{width:1200px;height:1000px;overflow:hidden}
body{background:var(--board);position:relative;font-family:"Arimo",Arial,sans-serif;color:var(--ink)}
.board-title{position:absolute;top:136px;left:0;width:1200px;text-align:center;font:700 31px "Libre Baskerville",Georgia,serif}
.side-label{position:absolute;top:264px;font:400 14px "Libre Baskerville",Georgia,serif;width:200px;text-align:center}
.side-label.front{left:268px}
.side-label.back{left:797px}
.flyer{position:absolute;top:296px;width:420px;height:596px;overflow:hidden;background:var(--paper)}
.flyer.front{left:133px}
.flyer.back{left:657px;border:1px solid #999}

/* front */
.hero-photo{position:absolute;left:0;top:0;width:420px;height:318px;background:linear-gradient(160deg,var(--photo-mid) 0%,var(--photo-light) 35%,#f2f4f8 70%,var(--photo-mid) 100%)}
.headline-band{position:absolute;left:0;top:318px;width:420px;height:103px;background:var(--band-grey)}
.service-panel{position:absolute;left:0;top:421px;width:420px;height:175px;background:var(--brand-blue)}
.portrait-ring{position:absolute;left:4px;top:278px;width:184px;height:184px;border-radius:50%;background:var(--band-grey)}
.portrait-photo{position:absolute;left:14px;top:288px;width:164px;height:164px;border-radius:50%;background:radial-gradient(circle at 45% 40%,#f3efe9 0%,#c9d4e2 55%,#7d97b5 100%)}
.headline-initial{position:absolute;left:197px;top:344px;color:#fff;font:400 64px "Great Vibes",cursive;line-height:1;white-space:nowrap}
.headline-rest{position:absolute;left:295px;top:353px;color:#fff;font:400 21px "Arimo",Arial,sans-serif;line-height:25px;white-space:nowrap}
.headline-rest span{display:block}
.service-list{position:absolute;left:192px;top:440px;list-style:none;color:#fff;font-size:12.5px;line-height:18px}
.service-list li{position:relative;padding-left:24px;margin-bottom:4.5px}
.service-list svg{position:absolute;left:0;top:3px}
.front-brand{position:absolute;left:36px;top:500px;width:120px;color:#fff;text-align:center}
.front-brand .name{font:400 13px "Arimo",Arial,sans-serif;line-height:15px}
.front-brand .name span{display:block;font-size:8px;letter-spacing:1.5px;margin-top:3px}
.front-badges{position:absolute;left:48px;top:542px;display:flex;gap:4px;align-items:center}
.badge{display:block;background:#ddd}
.badge.round{width:14px;height:14px;border-radius:50%}
.front-badges .divider{width:1px;height:16px;background:#fff;margin:0 3px}

/* back */
.feature{position:absolute;left:34px;width:370px}
.feature .dot{position:absolute;left:0;top:8px;width:46px;height:46px;border-radius:50%;background:var(--icon-grey)}
.feature h3{margin-left:77px;font:700 10px "Arimo",Arial,sans-serif;color:var(--heading-blue);margin-bottom:7px}
.feature p{margin-left:77px;font-size:7.6px;line-height:9.4px;color:var(--body-grey);width:278px}
.back-brand{position:absolute;left:110px;top:474px;font:400 11px "Arimo",Arial,sans-serif;color:var(--body-grey)}
.back-brand span{display:block;font-size:6.5px;letter-spacing:1.3px;margin-top:2px}
.contact{position:absolute;left:110px;top:514px;font-size:7.2px;line-height:9.3px;color:var(--body-grey)}
.contact strong{display:block}
.accreditations{position:absolute;left:278px;top:500px;width:110px;height:80px}
.accreditations .badge{position:absolute;background:#c9c9c9}
</style>
</head>
<body>
<h1 class="board-title">A5 Flyer</h1>
<div class="side-label front">FRONT</div>
<div class="side-label back">BACK</div>

<section class="flyer front">
  <div class="hero-photo" role="img" aria-label="Photo of a profit report with a bar chart, glasses and a pen"></div>
  <div class="headline-band"></div>
  <div class="service-panel"></div>
  <div class="portrait-ring"></div>
  <div class="portrait-photo" role="img" aria-label="Photo of two smiling professionals looking at a tablet"></div>
  <span class="headline-initial">M</span>
  <div class="headline-rest"><span>OST</span><span>TRUSTED</span></div>
  <ul class="service-list">
    <li><svg width="10" height="10" viewBox="0 0 10 10"><path d="M1 5.5l2.5 3L9 1" fill="none" stroke="#fff" stroke-width="1.8"/></svg>Boutique Accountancy Practice</li>
    <li><svg width="10" height="10" viewBox="0 0 10 10"><path d="M1 5.5l2.5 3L9 1" fill="none" stroke="#fff" stroke-width="1.8"/></svg>Chartered Accountant,</li>
    <li><svg width="10" height="10" viewBox="0 0 10 10"><path d="M1 5.5l2.5 3L9 1" fill="none" stroke="#fff" stroke-width="1.8"/></svg>Accountancy And<br>Bookkeeping Services</li>
    <li><svg width="10" height="10" viewBox="0 0 10 10"><path d="M1 5.5l2.5 3L9 1" fill="none" stroke="#fff" stroke-width="1.8"/></svg>Customized Service</li>
    <li><svg width="10" height="10" viewBox="0 0 10 10"><path d="M1 5.5l2.5 3L9 1" fill="none" stroke="#fff" stroke-width="1.8"/></svg>External Accountant.</li>
  </ul>
  <div class="front-brand">
    <div class="name">Torvela<span>FINANCIAL SERVICES</span></div>
  </div>
  <div class="front-badges">
    <span class="badge round"></span><span class="badge round"></span><span class="divider"></span><span class="badge round"></span>
  </div>
</section>

<section class="flyer back">
  <div class="feature" style="top:37px"><span class="dot"></span><h3>Boutique Accountancy Practice</h3><p>With extensive experience in preparing company accounts, we can not only take care of your bookkeeping, but also prepare your year-end accounts. This negates the need to have a separate bookkeeper and accountant and means your year-end financials are completed promptly and by someone who is very hands-on and understands your business.</p></div>
  <div class="feature" style="top:118px"><span class="dot"></span><h3>Boutique Accountancy Practice</h3><p>With extensive experience in preparing company accounts, we can not only take care of your bookkeeping, but also prepare your year-end accounts. This negates the need to have a separate bookkeeper and accountant and means your year-end financials are completed promptly and by someone who is very hands-on and understands your business.</p></div>
  <div class="feature" style="top:199px"><span class="dot"></span><h3>Boutique Accountancy Practice</h3><p>With extensive experience in preparing company accounts, we can not only take care of your bookkeeping, but also prepare your year-end accounts. This negates the need to have a separate bookkeeper and accountant and means your year-end financials are completed promptly and by someone who is very hands-on and understands your business.</p></div>
  <div class="feature" style="top:283px"><span class="dot"></span><h3>Boutique Accountancy Practice</h3><p>With extensive experience in preparing company accounts, we can not only take care of your bookkeeping, but also prepare your year-end accounts. This negates the need to have a separate bookkeeper and accountant and means your year-end financials are completed promptly and by someone who is very hands-on and understands your business.</p></div>
  <div class="feature" style="top:368px"><span class="dot"></span><h3>Boutique Accountancy Practice</h3><p>With extensive experience in preparing company accounts, we can not only take care of your bookkeeping, but also prepare your year-end accounts. This negates the need to have a separate bookkeeper and accountant and means your year-end financials are completed promptly and by someone who is very hands-on and understands your business.</p></div>

  <div class="back-brand">Torvela<span>FINANCIAL SERVICES</span></div>
  <div class="contact">
    <strong>ABN 12 345 678 901</strong>
    Suite 2, Level 3, 118 Harbour Street,<br>
    Kelmore, NSW 2090<br>
    Office: 02 9000 1234 • Mobile: 0400 000 111<br>
    Email: admin@torvela.com.au<br>
    <strong>www.torvela.com.au</strong>
  </div>
  <div class="accreditations">
    <span class="badge" style="left:0;top:14px;width:14px;height:14px;border-radius:50%;background:#d23b3b"></span>
    <span class="badge" style="left:0;top:40px;width:18px;height:16px"></span>
    <span class="badge" style="left:30px;top:40px;width:14px;height:14px"></span>
    <span class="badge" style="left:66px;top:36px;width:18px;height:18px;border-radius:50%;background:#1fa9dc"></span>
    <span class="badge" style="left:87px;top:36px;width:18px;height:18px;border-radius:50%"></span>
    <span class="badge" style="left:66px;top:58px;width:18px;height:6px;background:#6b3d8f"></span>
    <span class="badge" style="left:87px;top:58px;width:18px;height:6px;background:#d23b3b"></span>
  </div>
</section>
</body>
</html>
```